Herausgeber suchen Design
Zielgruppe
Wir sind Herausgeber einer Festschrift für unseren Doktor-/Habilvater, Prof. Dr. Wallmerk, und suchen ein hochwertiges Design für die Einladungskarten zu einem Symposium, im Rahmen dessen die Festschrift übergeben wird; Zielgruppe sind die Autoren der Festschrift, Alumnis und Weggefährten von Herrn Wallmerk
Aufgabenstellung
- Maße: 210 mm x 105 mm
- Einladungskarte: geklappt; Frontseite, 2 Innenseiten, Rückseite
- Zum Text siehe Datei 'Text Einladungskarte'
- Design eher traditionell/konservativ, da es sich um einen wissenschaftlichen Hintergrund handelt (Symposium, Übergabe Festschrift)
- Die Farben sollen mit dem Cover der Festschrift korrespondieren (vgl. Datei 'Templates_Research_Tessner', dort das erste Cover (TKM_PV_Q04)

```html
<!DOCTYPE html>
<html lang="de">
<head>
<meta charset="utf-8">
<title>Symposium – Einladung</title>
<link rel="stylesheet" href="https://fonts.googleapis.com/css2?family=Fira+Sans+Condensed:ital,wght@0,300;0,400;0,600;1,400;1,600&display=swap">
<style>
  :root {
    --blue: #0468b1;
    --navy: #1f2a50;
    --navy-mid: #3a4066;
    --white: #ffffff;
    --ink: #1f2a50;
  }
  html, body {
    margin: 0;
    padding: 0;
    width: 1200px;
    height: 1200px;
    overflow: hidden;
    background: var(--white);
  }
  .card {
    position: relative;
    width: 1240px;
    height: 1240px;
    transform: scale(0.967742);
    transform-origin: 0 0;
    font-family: "Fira Sans Condensed", "Arial Narrow", sans-serif;
    color: var(--white);
    overflow: hidden;
  }
  .backdrop { position: absolute; inset: 0; }
  .t { position: absolute; margin: 0; white-space: nowrap; line-height: 1; font-weight: 400; }
  .title { left: 108px; top: 62px; font-size: 82px; font-weight: 400; }
  .lead { left: 335px; font-size: 37px; }
  .address { left: 335px; top: 533px; font-size: 28px; }
  .editors-label, .editor { font-size: 29px; }
  .editors-label { left: 110px; }
  .col-a { left: 335px; }
  .col-b { left: 635px; }
  .invite { left: 335px; top: 780px; font-size: 29px; }
  .programme { color: var(--ink); font-size: 22px; }
  .programme-label { left: 220px; top: 862px; font-weight: 600; }
  .item { left: 335px; }
  .item::before {
    content: "";
    position: absolute;
    left: -14px; top: 9px;
    width: 5px; height: 5px;
    border-radius: 50%;
    background: var(--ink);
  }
  .speaker { left: 335px; font-style: italic; }
  .closing { left: 220px; top: 1133px; color: var(--ink); font-size: 22px; }
  .rsvp {
    position: absolute;
    left: 220px; top: 1180px;
    width: 800px; height: 60px;
    background: var(--navy);
    display: flex; align-items: center; justify-content: center;
    font-style: italic; font-weight: 600; font-size: 21px;
  }
</style>
</head>
<body>
<div class="card">
  <svg class="backdrop" width="1240" height="1240" viewBox="0 0 1240 1240" aria-hidden="true">
    <defs>
      <linearGradient id="fade" x1="0" y1="0" x2="0" y2="1">
        <stop offset="0" stop-color="#1f2a50"/>
        <stop offset="0.3" stop-color="#2a3358"/>
        <stop offset="0.48" stop-color="#5a5e82"/>
        <stop offset="0.65" stop-color="#b4b3c8"/>
        <stop offset="0.82" stop-color="#e6e5ee"/>
        <stop offset="0.92" stop-color="#ffffff"/>
      </linearGradient>
    </defs>
    <rect x="0" y="300" width="1240" height="940" fill="url(#fade)"/>
    <polygon points="0,0 1240,0 1240,305 60,365 60,310 0,312" fill="var(--blue)"/>
    <line x1="60" y1="0" x2="60" y2="590" stroke="#ffffff" stroke-width="2"/>
  </svg>

  <h1 class="t title">Symposium</h1>
  <p class="t lead" style="top:171px">anlässlich der Übergabe der Festschrift</p>
  <p class="t lead" style="top:221px">an Prof. Dr. Carl-Christian Wallmerk</p>

  <p class="t lead" style="top:389px">am 29. Juni 2018 um 16.00 Uhr</p>
  <p class="t lead" style="top:484px">im Gästehaus der Universität Nordhafen</p>
  <p class="t address">Lindenallee 12, 20999 Nordhafen</p>

  <p class="t editors-label" style="top:643px">Die Herausgeber</p>
  <p class="t editor col-a" style="top:643px">Prof. Dr. Henrik Valden</p>
  <p class="t editor col-a" style="top:683px">Prof. Dr. Jonas C. Werber</p>
  <p class="t editor col-a" style="top:723px">Dr. Andreas Marlow</p>
  <p class="t editor col-b" style="top:643px">Prof. Dr. Stefan Möllring</p>
  <p class="t editor col-b" style="top:683px">StB PD Dr. Jorrit Sanders</p>
  <p class="t invite">laden herzlich ein</p>

  <div class="programme">
    <p class="t programme-label">Ablauf</p>
    <p class="t item" style="top:862px">Begrüßung und Vorstellung der Festschrift</p>
    <p class="t speaker" style="top:892px">Prof. Dr. Henrik Valden</p>
    <p class="t item" style="top:928px">„Fortentwicklung des Corporate Governance Reportings“</p>
    <p class="t speaker" style="top:958px">Prof. Dr. Tobias C. Lerchner, LL.M. (London)</p>
    <p class="t item" style="top:994px">Diskussion</p>
    <p class="t item" style="top:1030px">„Neuere Entwicklungen im Rahmen der risikoorientierten Abschlussprüfung"</p>
    <p class="t speaker" style="top:1060px">Prof. Dr. Philipp E. Zeltner</p>
    <p class="t item" style="top:1097px">Diskussion</p>
  </div>
  <p class="t closing">Im Anschluss an das Symposium findet ein Umtrunk statt.</p>

  <div class="rsvp">Um Antwort wird gebeten bis zum 18. Mai 2018 unter birgit.arndt@wiso.uni-nordhafen.de</div>
</div>
</body>
</html>
```